Graphic to communicate emotional connection

Howdy-I need a graphic that describe my financial planning process.The attached is a concept, but please use your own creativity to show how you would display this:- The four circles on the outside (Protect what we have, know where it goes, make it grow, and dignity and independence) are the four major areas of concern- Then, there are three value statements:- The first is the most powerful which is that Clarity leads to Control which allows your Intentions to come through- The second shows that we take our clients from Uncertainty and Confusion, to Confidence and Intention- The third says we create space for you to develop your Purposeful Effort which leads to Your Best Financial Life.I've also attached my logo - please use the colors in my logo and maybe add a soft green as needed.The reader should be able to briefly scan this document and understand that we will connect with them on an emotional level to get their finances in shape.Thanks!-Ned

Target Market(s)

wealthy women, whether independent or married

Industry/Entity Type

Financial Planning

Requirements
Must have
• Please use the colors in my logo plus a soft green as needed
Should not have
• This should not be a busy or hard-to-read graphic. It is meant to convey an that I try to make an emotional connection, at a glance.

```html
<!DOCTYPE html>
<html lang="en">
<head>
<meta charset="utf-8">
<title>Our Aspiration</title>
<link rel="stylesheet" href="https://fonts.googleapis.com/css2?family=Questrial&display=swap">
<style>
  :root {
    --navy-deep: #021f5b;
    --navy-bright: #042c70;
    --ink: #0b2b74;
    --band-grey: #636363;
    --figure-grey: #414448;
    --white: #ffffff;
    --mint: #4ff08c;
  }
  * { margin: 0; padding: 0; box-sizing: border-box; }
  html, body { width: 1200px; height: 1166px; overflow: hidden; }
  body { font-family: "Questrial", "Century Gothic", sans-serif; }
  .canvas {
    position: relative; width: 1200px; height: 1166px; overflow: hidden;
    background: linear-gradient(to right, var(--navy-deep) 0 643px, var(--navy-bright) 643px 100%);
  }
  .band {
    position: absolute; left: 0; width: 1200px; height: 71px;
    background: var(--band-grey); color: var(--white);
  }
  .band--top { top: 26px; display: flex; align-items: center; justify-content: center; }
  .band--bottom { top: 1073px; }
  .title { font-size: 37px; font-weight: 400; letter-spacing: 3.5px; padding-left: 4px; }
  .step { position: absolute; top: 14px; font-size: 36px; letter-spacing: 3px; transform: translateX(-50%); line-height: 44px; white-space: nowrap; }
  .shapes { position: absolute; inset: 0; }
  .concern {
    position: absolute; left: 49px; color: var(--ink);
    font-size: 28px; line-height: 35px; text-transform: uppercase;
  }
  .figure { position: absolute; border-radius: 26px 26px 8px 8px; }
  .figure--grey { background: var(--figure-grey); }
  .figure--light { background: rgba(255,255,255,0.9); }
  .promise {
    position: absolute; width: 160px; left: 425px; text-align: center;
    color: var(--white); font-size: 29px; line-height: 35px;
  }
  .state {
    position: absolute; left: 643px; color: var(--ink);
    font-size: 25px; line-height: 31px; text-transform: uppercase;
  }
  .outcome {
    position: absolute; width: 190px; text-align: center; color: var(--white);
    font-size: 23px; line-height: 28px; text-transform: uppercase; letter-spacing: 1px;
  }
  .connector { position: absolute; left: 881px; color: var(--white); font-size: 29px; }
</style>
</head>
<body>
<main class="canvas">
  <header class="band band--top"><h1 class="title">OUR ASPIRATION</h1></header>

  <svg class="shapes" width="1200" height="1166" viewBox="0 0 1200 1166" aria-hidden="true">
    <g class="concern-arrows" fill="var(--white)">
      <polygon points="20,130 266,130 333,237 266,344 20,344"/>
      <polygon points="20,362 266,362 333,469 266,576 20,576"/>
      <polygon points="20,594 266,594 333,701 266,808 20,808"/>
      <polygon points="20,826 266,826 333,933 266,1040 20,1040"/>
    </g>

    <g class="promise-arrows">
      <polygon points="554,374 812,374 868,470 812,567 554,567" fill="var(--white)"/>
      <polygon points="554,587 812,587 868,683 812,780 554,780" fill="var(--white)"/>
      <circle cx="531" cy="470" r="97" fill="var(--navy-deep)"/>
      <circle cx="531" cy="683" r="97" fill="var(--navy-deep)"/>
    </g>

    <g class="rings" fill="none" stroke="var(--mint)">
      <circle cx="505" cy="469" r="99" stroke-width="2"/>
      <circle cx="507" cy="470" r="94" stroke-width="1.3"/>
      <circle cx="503" cy="468" r="89" stroke-width="1.3"/>
      <circle cx="505" cy="682" r="99" stroke-width="2"/>
      <circle cx="507" cy="683" r="94" stroke-width="1.3"/>
      <circle cx="503" cy="681" r="89" stroke-width="1.3"/>
      <circle cx="1061" cy="336" r="108" stroke-width="2"/>
      <circle cx="1059" cy="337" r="103" stroke-width="1.3"/>
      <circle cx="1063" cy="335" r="96" stroke-width="1.3"/>
      <circle cx="1054" cy="830" r="108" stroke-width="2"/>
      <circle cx="1052" cy="831" r="103" stroke-width="1.3"/>
      <circle cx="1056" cy="829" r="96" stroke-width="1.3"/>
    </g>

    <g class="connectors" fill="none" stroke="var(--mint)" stroke-width="1.8" stroke-linecap="round" stroke-linejoin="round">
      <path d="M348,342 L412,408"/>
      <path d="M348,812 L412,746"/>
      <path d="M886,436 L948,398 M936,396 L948,398 L944,410"/>
      <path d="M886,710 L948,748 M944,736 L948,748 L936,750"/>
    </g>
  </svg>

  <p class="concern" style="top:187px">Protect<br>what we<br>have</p>
  <p class="concern" style="top:433px">Make it<br>grow</p>
  <p class="concern" style="top:649px">Know<br>where<br>it goes</p>
  <p class="concern" style="top:872px">Dignity<br>and<br>indepen-<br>dence</p>

  <div class="figure figure--grey" role="img" aria-label="Silhouette of a standing woman" style="left:205px;top:155px;width:48px;height:163px"></div>
  <div class="figure figure--grey" role="img" aria-label="Silhouette of a businesswoman walking" style="left:206px;top:383px;width:46px;height:163px"></div>
  <div class="figure figure--grey" role="img" aria-label="Silhouette of a woman with arms crossed" style="left:202px;top:613px;width:46px;height:167px"></div>
  <div class="figure figure--grey" role="img" aria-label="Silhouette of a woman in a skirt suit" style="left:201px;top:847px;width:46px;height:164px"></div>
  <div class="figure figure--light" role="img" aria-label="Silhouette of a confident businesswoman wearing a crown" style="left:1030px;top:503px;width:72px;height:174px"></div>

  <p class="promise" style="top:431px">we take<br>you from</p>
  <p class="promise" style="top:642px">we create<br>space for<br>you</p>

  <p class="state" style="top:442px">Uncertainty<br>Confusion</p>
  <p class="state" style="top:657px">Purposeful<br>Effort</p>

  <p class="connector" style="top:362px">to</p>
  <p class="connector" style="top:750px">to</p>

  <p class="outcome" style="left:966px;top:314px">Confidence<br>Intention</p>
  <p class="outcome" style="left:959px;top:790px">Your best<br>financial<br>life</p>

  <footer class="band band--bottom">
    <svg class="shapes" width="1200" height="71" viewBox="0 0 1200 71" aria-hidden="true">
      <polygon points="374,0 394,0 423,35.5 394,71 374,71 403,35.5" fill="var(--white)"/>
      <polygon points="766,0 787,0 817,35.5 787,71 766,71 796,35.5" fill="var(--white)"/>
    </svg>
    <span class="step" style="left:213px">CLARITY</span>
    <span class="step" style="left:597px">CONTROL</span>
    <span class="step" style="left:999px">INTENTIONS</span>
  </footer>
</main>
</body>
</html>
```